Velko Prime seamless gutters and drains

I need a cool, modern, sleek design for m-370 crew cab trucks and 16’ box trucks. I’m not wanting full wraps but I want like a half wrap in the center of the vehicles. Blue background with white logo. With website and phone number only.

velkoprime.example
317.804.2196

Target Market(s)

Homeowners and contractors

Industry/Entity Type

Seamless gutters and drainage

Font styles to use
Sans Serif

Colors
0054AA
0677BA
7BADD7
CADEEF
E8F1F8

Requirements
Must have
• Blue background with white logo and white lettering
Nice to have
• Blue background with curvatures and white logo and lettering in the middle of the box truck and m-370’s

```html
<!DOCTYPE html>
<html lang="en">
<head>
<meta charset="utf-8">
<title>Velko Prime – Vehicle Graphics</title>
<link href="https://fonts.googleapis.com/css2?family=Lexend:wght@500;700&display=swap" rel="stylesheet">
<style>
  :root {
    --blue-deep: #0054AA;
    --blue-mid: #0677BA;
    --blue-light: #7BADD7;
    --blue-pale: #CADEEF;
    --blue-mist: #E8F1F8;
    --white: #ffffff;
    --page: #f4f6f9;
  }
  * { margin: 0; padding: 0; box-sizing: border-box; }
  html, body { width: 883px; height: 1200px; overflow: hidden; }
  body {
    background: var(--page);
    font-family: "Lexend", sans-serif;
    position: relative;
  }
  .wrap-panel {
    position: absolute;
    left: 30px;
    width: 823px;
    background: var(--white);
    overflow: hidden;
    box-shadow: 0 2px 10px rgba(0, 40, 90, 0.12);
  }
  .wrap-panel--box { top: 70px; height: 395px; }
  .wrap-panel--crew { top: 560px; height: 330px; }
  .wrap-panel svg.band { position: absolute; inset: 0; width: 100%; height: 100%; }

  .contact { position: absolute; list-style: none; }
  .contact__item {
    display: flex; align-items: center;
    color: var(--blue-deep);
    font-weight: 700;
  }
  .contact__icon {
    flex: none;
    border: 2px solid var(--blue-deep);
    display: flex; align-items: center; justify-content: center;
  }
  .wrap-panel--box .contact { left: 28px; top: 38px; }
  .wrap-panel--box .contact__item { font-size: 23px; gap: 14px; margin-bottom: 20px; }
  .wrap-panel--box .contact__icon { width: 24px; height: 24px; }
  .wrap-panel--crew .contact { left: 34px; top: 34px; }
  .wrap-panel--crew .contact__item { font-size: 16px; gap: 10px; margin-bottom: 12px; }
  .wrap-panel--crew .contact__icon { width: 17px; height: 17px; border-width: 1.5px; }
  .contact__icon svg { width: 72%; height: 72%; }

  .brand { position: absolute; color: var(--white); text-align: left; }
  .brand__name { font-weight: 700; line-height: 1; display: block; }
  .brand__tagline { font-weight: 500; letter-spacing: 0.12em; display: block; color: var(--white); }
  .wrap-panel--box .brand { left: 64px; top: 258px; }
  .wrap-panel--box .brand__name { font-size: 44px; }
  .wrap-panel--box .brand__tagline { font-size: 11px; margin-top: 8px; padding-left: 4px; }
  .wrap-panel--crew .brand { left: 300px; top: 248px; }
  .wrap-panel--crew .brand__name { font-size: 28px; }
  .wrap-panel--crew .brand__tagline { font-size: 8px; margin-top: 5px; padding-left: 2px; }

  .splash-art {
    position: absolute;
    border-radius: 46% 54% 40% 60% / 50% 45% 55% 50%;
    background: radial-gradient(circle at 45% 45%, var(--blue-mist) 0%, var(--blue-light) 45%, var(--blue-mid) 100%);
    opacity: 0.9;
  }
  .wrap-panel--box .splash-art { left: 590px; top: 60px; width: 225px; height: 270px; }
  .wrap-panel--crew .splash-art { left: 560px; top: 120px; width: 150px; height: 175px; }
</style>
</head>
<body>

  <section class="wrap-panel wrap-panel--box" aria-label="Box truck side graphic">
    <svg class="band" viewBox="0 0 823 395" preserveAspectRatio="none" aria-hidden="true">
      <path d="M0 215 C 160 300 420 230 823 0 L823 395 L0 395 Z" fill="var(--blue-deep)"/>
    </svg>
    <ul class="contact">
      <li class="contact__item">
        <span class="contact__icon"><svg viewBox="0 0 24 24"><path d="M6.6 10.8a15 15 0 0 0 6.6 6.6l2.2-2.2c.3-.3.7-.4 1-.2 1.1.4 2.3.6 3.6.6.6 0 1 .4 1 1V20c0 .6-.4 1-1 1A17 17 0 0 1 3 4c0-.6.4-1 1-1h3.5c.6 0 1 .4 1 1 0 1.3.2 2.5.6 3.6.1.3 0 .7-.2 1z" fill="var(--blue-deep)"/></svg></span>
        317.804.2196
      </li>
      <li class="contact__item">
        <span class="contact__icon"><svg viewBox="0 0 24 24" fill="none" stroke="var(--blue-deep)" stroke-width="2"><circle cx="12" cy="12" r="9"/><path d="M3 12h18M12 3c3 3.5 3 14.5 0 18M12 3c-3 3.5-3 14.5 0 18"/></svg></span>
        velkoprime.example
      </li>
    </ul>
    <div class="splash-art" role="img" aria-label="Illustration of large glossy blue water droplets splashing"></div>
    <div class="brand">
      <span class="brand__name">Velko Prime</span>
      <span class="brand__tagline">GUTTERS | DRAINS</span>
    </div>
  </section>

  <section class="wrap-panel wrap-panel--crew" aria-label="Crew cab truck side graphic">
    <svg class="band" viewBox="0 0 823 330" preserveAspectRatio="none" aria-hidden="true">
      <path d="M0 258 C 120 255 210 232 290 205 C 440 158 600 120 823 95 L823 330 L0 330 Z" fill="var(--blue-deep)"/>
    </svg>
    <ul class="contact">
      <li class="contact__item">
        <span class="contact__icon"><svg viewBox="0 0 24 24"><path d="M6.6 10.8a15 15 0 0 0 6.6 6.6l2.2-2.2c.3-.3.7-.4 1-.2 1.1.4 2.3.6 3.6.6.6 0 1 .4 1 1V20c0 .6-.4 1-1 1A17 17 0 0 1 3 4c0-.6.4-1 1-1h3.5c.6 0 1 .4 1 1 0 1.3.2 2.5.6 3.6.1.3 0 .7-.2 1z" fill="var(--blue-deep)"/></svg></span>
        317.804.2196
      </li>
      <li class="contact__item">
        <span class="contact__icon"><svg viewBox="0 0 24 24" fill="none" stroke="var(--blue-deep)" stroke-width="2"><circle cx="12" cy="12" r="9"/><path d="M3 12h18M12 3c3 3.5 3 14.5 0 18M12 3c-3 3.5-3 14.5 0 18"/></svg></span>
        velkoprime.example
      </li>
    </ul>
    <div class="splash-art" role="img" aria-label="Illustration of glossy blue water droplets splashing"></div>
    <div class="brand">
      <span class="brand__name">Velko Prime</span>
      <span class="brand__tagline">GUTTERS | DRAINS</span>
    </div>
  </section>

</body>
</html>
```